Hollywood copywriter needs to drop a lot of names.

I want a one-page flyer that uses my extensive industry experience to wow potential clients.
With one glance, a busy entertainment professional should get a sense of the breadth and quality of my previous work, without actually seeing any of it. The titles and brand names speak for themselves.
The flyer will be heavy on text, but I don’t want it to look like a traditional resume. Use graphic elements to make it feel personal, memorable and fun to read.
Confident and creative is good. Not corporate or flashy.
No movie or TV cliches!
Must be easy to share via email.
Photoshop file is a rough proof-of-concept with all content to be included. Should not be considered a template or limitation. Just a starting point.
Updates
Need extra days to review
Industry/Entity Type
Entertainment
Colors
Designer to choose colors to be used in the design.
Look and feel

```html
<!DOCTYPE html>
<html lang="en">
<head>
<meta charset="utf-8">
<title>Dale Harmon – Writer – Branding &amp; Advertising</title>
<link rel="stylesheet" href="https://fonts.googleapis.com/css2?family=Oswald:wght@400;500&family=Montserrat:wght@700&family=Arimo:wght@400&family=Open+Sans:wght@400&display=swap">
<style>
  :root {
    --page-bg: #e6e7e9;
    --paper: #ffffff;
    --royal: #0b55a8;
    --sky: #0a88c9;
    --navy: #1d3b85;
    --deep: #0d2f78;
    --panel: #ececec;
    --ink: #1b1b1b;
    --white: #ffffff;
  }
  * { margin: 0; padding: 0; box-sizing: border-box; }
  html, body { width: 1200px; height: 1200px; overflow: hidden; background: var(--page-bg); }
  .canvas { position: relative; width: 1200px; height: 1200px; }
  .flyer {
    position: absolute; left: 391px; top: 75px;
    width: 525px; height: 1312px;
    background: var(--paper);
    transform: scale(0.8); transform-origin: top left;
    overflow: hidden;
    box-shadow: 0 4px 14px rgba(0,0,0,.18);
  }
  .flyer-shapes { position: absolute; left: 0; top: 0; width: 525px; height: 1312px; }
  .identity {
    position: absolute; left: 44px; top: 38px; width: 188px; height: 188px;
    display: flex; flex-direction: column; align-items: center; justify-content: center;
    color: var(--white); font-family: "Oswald", sans-serif; text-align: center;
  }
  .identity-name { font-size: 31px; font-weight: 400; line-height: 1; }
  .identity-role { font-size: 22px; font-weight: 400; line-height: 1.2; margin-top: 3px; }
  .headline {
    position: absolute; left: 222px; top: 182px; width: 282px; text-align: center;
    font-family: "Montserrat", sans-serif; font-weight: 700; color: var(--royal);
    font-size: 30px; line-height: 37px; letter-spacing: .5px;
  }
  .credit-title {
    position: absolute; top: 294px; height: 16px; width: 98px; background: var(--navy);
    color: var(--white); font-family: "Oswald", sans-serif; font-size: 9.5px; font-weight: 500;
    line-height: 16px; padding-left: 11px; white-space: nowrap;
  }
  .credit-panel { position: absolute; top: 320px; background: var(--panel); padding: 7px 0 0 12px; overflow: hidden; }
  .credit-list { list-style: none; font-family: "Open Sans", sans-serif; font-size: 5.2px; line-height: 9.2px; color: var(--ink); white-space: nowrap; }
  .services {
    position: absolute; left: 296px; top: 996px; width: 240px; text-align: center;
    list-style: none; font-family: "Arimo", sans-serif; font-size: 15px; line-height: 23.4px; color: var(--white);
  }
  .contact { position: absolute; top: 1266px; left: 0; width: 525px; height: 16px;
    color: var(--white); font-family: "Arimo", sans-serif; font-size: 11.5px; line-height: 16px; }
  .contact span, .contact svg { position: absolute; top: 0; }
  .contact-icon { width: 16px; height: 16px; }
</style>
</head>
<body>
<div class="canvas">
  <article class="flyer">
    <svg class="flyer-shapes" viewBox="0 0 525 1312" aria-hidden="true">
      <path d="M0 0 H525 V82 C450 78 360 118 280 160 C230 186 200 190 160 170 C110 145 60 100 0 52 Z" fill="var(--royal)"/>
      <path d="M0 52 C40 90 80 118 120 138 C80 128 40 110 0 90 Z" fill="var(--deep)"/>
      <path d="M0 60 C30 80 60 98 95 118" fill="none" stroke="#ffffff" stroke-width="2"/>
      <path d="M335 140 C400 100 455 86 525 88 V120 C455 114 400 118 335 140 Z" fill="var(--deep)"/>
      <circle cx="138" cy="133" r="94" fill="var(--sky)"/>
      <path d="M0 1246 C120 1205 260 1200 525 1245 V1312 H0 Z" fill="var(--sky)"/>
      <path d="M86 1222 C170 1200 260 1195 360 1210 C270 1204 180 1208 86 1230 Z" fill="var(--navy)"/>
    </svg>

    <header class="identity">
      <div class="identity-name">DALE HARMON</div>
      <div class="identity-role">Writer</div>
    </header>
    <h1 class="headline">BRANDING &amp;<br>ADVERTISING</h1>

    <section class="credit-col">
      <div class="credit-title" style="left:23px;">100+ MOVIES</div>
      <div class="credit-panel" style="left:24px;width:117px;height:879px;">
        <ul class="credit-list">
          <li>Tin Lantern</li><li>Nine Willows</li><li>Harbor of Keys</li><li>Paper Comets</li><li>Marlow Lane</li><li>Velvet Quarry</li><li>Amber Orchard</li><li>Far Pennant</li><li>Juniper Drive</li><li>Copper Canyon Kids</li><li>Owl Meadow</li><li>Glass Kettle</li><li>Silver Thimble</li><li>Dusty Pelican</li><li>Last Carousel</li><li>Kite and Crane</li><li>Briar Tower</li><li>Wild Parsnip</li><li>Lantern Falls</li><li>Pebble Garden</li><li>Lake Marrow</li><li>Hollow Fiddle</li><li>Winter Beehive</li><li>Small Ferns</li><li>Seabrook Summer</li><li>Moon Pickle</li><li>Salt Marigold</li><li>Ember Cove</li><li>Feather Drop</li><li>Tall Buttons</li><li>Lucky Walrus</li><li>Dapple Stable</li><li>Long Ladder</li><li>Side Pocket Saga</li><li>Neon Cactus</li><li>Rusty Anchor</li><li>Greenwick</li><li>Half Lemon</li><li>Echo Spruce</li><li>Quill and Ink</li><li>Storm Basket</li><li>North Thistle</li><li>Sky Pudding</li><li>Cobble Case</li><li>Big Meadowlark</li><li>Calm Dunes</li><li>Jetty Song</li><li>Cloud Bakery</li><li>Wild Marble</li><li>Fair Otter</li><li>Back Lot Blues</li><li>River Whistle</li><li>Crossbill Creek</li><li>Pale Lantern</li><li>Deep Thicket</li><li>Sand Pony</li><li>Main Street Mice</li><li>Paper Falcon</li><li>Last Lullaby</li><li>Open Acorn</li><li>Sun Pickers</li><li>Night Wren</li><li>Fire Fern</li><li>Crosstown Kettle</li><li>Third Lantern</li><li>Kite Season</li><li>Grey Mitten</li><li>Blind Badger</li><li>Hard Cider Hill</li><li>Zero Acre</li><li>Safe Pier</li><li>Twin Oars</li><li>Gold Gravel</li><li>Slow Ember</li><li>Star Pasture</li><li>Bay Window Bell</li><li>Hot Tin Tuesday</li><li>Cool Pebble</li><li>Ghost Orchard</li><li>Iron Daisy</li><li>Mad Marmalade</li><li>Sea Muffin</li><li>Long Lanyard</li><li>Red Lichen</li><li>Wild Westerly</li><li>Blue Biscuit</li><li>Home Hollow</li><li>Sly Parakeet</li><li>Cat Lantern</li><li>Wolf Whistle Way</li><li>Top Floor Tango</li><li>Sky Juniper</li><li>True Pinecone</li><li>Sweet Quarry</li><li>Clear Harbor</li>
        </ul>
      </div>
    </section>

    <section class="credit-col">
      <div class="credit-title" style="left:159px;">120+ TV SHOWS</div>
      <div class="credit-panel" style="left:156px;width:105px;height:869px;">
        <ul class="credit-list">
          <li>Thirty Lanterns</li><li>After the Parade</li><li>Alpaca Squad</li><li>Family Pickle</li><li>Angel Orchard</li><li>Trade Sparrows</li><li>Motel Marigold</li><li>Straight Spruce</li><li>Boarding Kettle</li><li>Body of Brambles</li><li>Border Lantern</li><li>Family Tablecloth</li><li>Bad Biscuit</li><li>Break Pine</li><li>Big Brambles</li><li>Short Thistle</li><li>Cake Lagoon</li><li>News Pelican</li><li>Coal Cottage</li><li>Coma Quilt</li><li>Late Owl</li><li>Cool Gravel</li><li>Damage Daisy</li><li>Degree Dune</li><li>Bounty Lane</li><li>Doc Wren</li><li>Dead Serious Sam</li><li>Marla Tonight</li><li>Extreme Attics</li><li>Feed the Ferrets</li><li>Flight Kettle</li><li>Food Fable</li><li>Full Acorn</li><li>Frontal Fern</li><li>Good Morning Pier</li><li>Game Gazebo</li><li>Fame Meadow</li><li>Hap and Hazel</li><li>Pawn Parlor</li><li>Home Thimble</li><li>Inside Orchard</li><li>Sunny Sprocket</li><li>Dead Mitten</li><li>Nerd Pavilion</li><li>Old Larkspur</li><li>Legends of Loam</li><li>Mankind Mosaic</li><li>First Lantern</li><li>Win a Walrus</li><li>Sitcom Sparrow</li><li>Rough Marble</li><li>Hockey Hollow</li><li>Fine Tuning Tom</li><li>New Ink Inn</li><li>Strange Acre</li><li>Parent Pantry</li><li>Corner Kettle</li><li>Bulls and Buttons</li><li>Pike Ward</li><li>Real Talk Rita</li><li>Second Spruce</li><li>Red Dormouse</li><li>Rogue Pebble</li><li>Royal Pantry</li><li>Award Willow</li><li>Our Small Business</li><li>Southern Skillet</li><li>Storage Pelicans</li><li>The Footbridge</li><li>Cell Lantern</li><li>Chat Meadow</li><li>The Polisher</li><li>Daily Grindstone</li><li>Pest Pavilion</li><li>First Thicket</li><li>Good Neighbor Nell</li><li>Word Marble</li><li>League Lantern</li><li>Peace Pickle</li><li>Porch Wives Club</li><li>Returned to Roost</li><li>Secret Spruce</li><li>Secret Thimbles</li><li>Starter Cottage</li><li>Walking Willow</li><li>Extreme Kites</li><li>Those Kettle Kids</li><li>Tiny Gazebo</li><li>Bayou Biscuit</li><li>Warrior Wren</li><li>Garden Gravel</li><li>Dog Parlor</li><li>Best Ferret</li><li>Night Larkspur</li>
        </ul>
      </div>
    </section>

    <section class="credit-col">
      <div class="credit-title" style="left:277px;">NETWORKS &amp; STUDIOS</div>
      <div class="credit-panel" style="left:277px;width:105px;height:620px;">
        <ul class="credit-list">
          <li>Larkfield Pictures</li><li>Quillstone TV</li><li>Channel Marigold</li><li>Hearthside Family</li><li>Ambervale Films</li><li>Antenna Wren</li><li>Pinegate Sports</li><li>Bluecrest News</li><li>Marrow Broadcast</li><li>Thistle Country</li><li>Kestrel News</li><li>Lanternview</li><li>Orchard One</li><li>Sproutling TV</li><li>Dunmore Studio</li><li>Channel Pebble</li><li>Kettle Kitchen</li><li>Channel Ferro</li><li>Channel Fernhill</li><li>Wrenly</li><li>Quizbell Net</li><li>Gallow Media</li><li>Brookheart TV</li><li>Velvet One</li><li>Velvet Asia</li><li>Trellis Home</li><li>Chronicle Hollow</li><li>Reelwick</li><li>Grandscope</li><li>Netherby</li><li>Ripple TV</li><li>Sage Women</li><li>Pixwell</li><li>Daybreak News</li><li>Terra Atlas</li><li>Meridian Media</li><li>Mundial Wren</li><li>Streamfield</li><li>Gridiron Hollow</li><li>Ourtown Network</li><li>Spoolhouse</li><li>Nebula Net</li><li>Beaker TV</li><li>Inkwell Media</li><li>Gallery TV</li><li>Fernhill Television</li><li>Stage Thirty</li><li>Starling Channel</li><li>Tailor TV</li><li>Station Juniper</li><li>Vintage Reel</li><li>Racquet TV</li><li>Marquee Net</li><li>Lessonbox TV</li><li>Doodle Time</li><li>Compass Travel</li><li>Verity Crime</li><li>Turnstile TV</li><li>Vireo Net</li><li>Prairie TV</li><li>Hitchwell One</li><li>Lumen Women</li><li>Wexford Network</li><li>Tempo One</li><li>Cubby Plus</li>
        </ul>
      </div>
    </section>

    <section class="credit-col">
      <div class="credit-title" style="left:398px;">TECH &amp; PRODUCTS</div>
      <div class="credit-panel" style="left:397px;top:311px;width:104px;height:620px;padding-top:16px;">
        <ul class="credit-list">
          <li>Alderwick</li><li>Brightfold</li><li>Calloway Toys</li><li>Dunmere Spirits</li><li>Emberline</li><li>Fenwick Audio</li><li>Glenora</li><li>Hollyfizz</li><li>Ivorycrest</li><li>Jaspen Wear</li><li>Kestrel Search</li><li>Lumora</li><li>Marquee Exchange</li><li>Norwell Data</li><li>Orbit Racers</li><li>Pellham Print</li><li>Quarto Books</li><li>Rivet Sound</li><li>Solenne Motors</li><li>Tandry Soft</li><li>Umberly</li><li>Velcourt</li><li>Wickham Parts</li><li>Xavora Pay</li><li>Yarrowell</li><li>Zephyrine</li><li>Ashgrove</li><li>Birchlane</li><li>Cobbler Tacos</li><li>Driftmart</li><li>Elmtree Kids</li><li>Fable Shoes</li><li>Granton Auto</li><li>Halcyon Card</li><li>Inkmere Events</li><li>Juno Chat</li><li>Kinloch</li>
        </ul>
      </div>
    </section>

    <svg class="flyer-shapes" viewBox="0 0 525 1312" aria-hidden="true">
      <circle cx="445" cy="1091" r="170" fill="var(--sky)"/>
      <circle cx="440" cy="1093" r="157" fill="var(--navy)"/>
    </svg>

    <ul class="services">
      <li>TV Spots</li>
      <li>Print &amp; Digital Ads</li>
      <li>Out Of Home</li>
      <li>Social Media Campaigns</li>
      <li>Sales Videos</li>
      <li>Mission Statements</li>
      <li>Brand Bibles</li>
      <li>Name Development</li>
    </ul>

    <footer class="contact">
      <span style="left:36px;">CONTACT US</span>
      <svg class="contact-icon" style="left:136px;" viewBox="0 0 16 16" aria-hidden="true"><path d="M1 6 L8 1 L15 6 V15 H1 Z" fill="none" stroke="#fff" stroke-width="1.4" stroke-linejoin="round"/><path d="M1 6 L8 11 L15 6" fill="none" stroke="#fff" stroke-width="1.4"/></svg>
      <span style="left:161px;font-size:10.5px;">daleharmon@mail.com</span>
      <svg class="contact-icon" style="left:285px;" viewBox="0 0 16 16" aria-hidden="true"><path d="M4 1.5 L6 5 L4.6 6.6 C5.5 8.6 7.4 10.5 9.4 11.4 L11 10 L14.5 12 L13 14.5 C7 14.5 1.5 9 1.5 3 Z" fill="#fff"/></svg>
      <span style="left:314px;font-size:10.5px;">555 014 0148</span>
    </footer>
  </article>
</div>
</body>
</html>
```